Webdesign für Selbsthilfegruppe für Gehörlose
Zielgruppe
(Un)gesehene Schwestern Chemnitz und Umgebung ist eine Selbsthilfegruppe
Wir sind eine Gruppe von Frauen mit und ohne Hörschädigungen sowie Traumaerfahrungen.
Die SHG berät allen Arten der Hörschädigung und Traumafolgen von betroffene Frauen.
Schwerpunkte der Arbeit:
Zurück in das ICH finden mit Unterstützung, Aufklärung, Erkennen, Benennen, Handlen und Vermittlung von Behandlungen sowie Rehabilitation und Rückfallprävention
Weiteres entnehmen Sie bitte aus dem Flyer
Aufgabenstellung
Barrierefreiheit der Website für Menschen mit Hörbehinderung

```html
<!DOCTYPE html>
<html lang="de">
<head>
<meta charset="utf-8">
<title>(Un)gesehene Schwestern Chemnitz und Umgebung</title>
<link rel="stylesheet" href="https://fonts.googleapis.com/css2?family=Quicksand:wght@400;500;600&display=swap">
<style>
:root{
  --purple:#c56ae6;
  --purple-soft:#f5d4fb;
  --pink-band:#f7d2fb;
  --green-band:#7be3a5;
  --green-dark:#46b083;
  --green-text:#3fae80;
  --ink:#2f2f35;
  --white:#ffffff;
}
*{box-sizing:border-box;margin:0;padding:0}
html,body{width:1200px;height:2708px;overflow:hidden;background:var(--white)}
body{position:relative;font-family:"Quicksand",sans-serif;color:var(--ink)}
h1,h2,h3{font-weight:400}
.abs{position:absolute}
.btn-contact{left:1011px;top:39px;width:136px;height:56px;border-radius:12px;background:var(--purple);color:var(--white);font-size:22px;display:flex;align-items:center;justify-content:center}
.brand{left:500px;top:46px;width:200px;height:160px;display:flex;flex-direction:column;align-items:center;justify-content:center;gap:8px;text-align:center}
.brand-dot{width:22px;height:22px;border-radius:50%;background:var(--ink)}
.brand-name{font-size:14px;font-weight:500;line-height:1.3;color:var(--ink)}
.nav a{position:absolute;transform:translateX(-50%);font-size:21px;color:var(--ink);text-decoration:none;white-space:nowrap}
.hero-bg{left:0;top:420px;width:1200px;height:420px;background:radial-gradient(ellipse 560px 200px at 600px 210px,#fbf0fd 0%,#fdf8fe 60%,#ffffff 100%)}
.hero-title{left:172px;top:480px;font-size:33px;color:var(--purple)}
.hero-sub{left:172px;top:543px;font-size:25px;line-height:31px}
.hero-text{left:172px;top:630px;width:422px;font-size:13.5px;line-height:15.8px}
.hero-date{left:172px;top:750px;font-size:13.5px;color:var(--green-text)}
.illus{border-radius:18px}
.section-title{left:0;width:1200px;top:922px;text-align:center;font-size:33px;color:var(--purple)}
.card{background:var(--purple-soft);border-radius:8px;font-size:13.5px;line-height:15.8px;padding:8px 13px}
.card-phone{display:flex;align-items:center;gap:12px;padding:0 14px;white-space:nowrap}
.mail{left:432px;top:1268px;width:336px;height:42px;border-radius:8px;background:var(--purple);color:var(--white);font-size:14px;display:flex;align-items:center;justify-content:center;gap:12px;white-space:nowrap}
.band-green{left:0;top:1445px;width:410px;height:439px;background:var(--green-band)}
.band-pink{left:410px;top:1445px;width:790px;height:439px;background:var(--pink-band)}
.focus-title{left:50px;top:1557px;font-size:26px}
.focus-text{left:50px;top:1629px;width:350px;font-size:13.5px;line-height:15.8px}
.goals-title{left:460px;top:1495px;font-size:26px;line-height:31px}
ul{list-style:none}
ul li{position:relative;padding-left:12px}
ul li::before{content:"•";position:absolute;left:0}
.focus-text ul{margin-top:16px;margin-left:8px}
.goals-list{left:468px;top:1598px;width:340px;font-size:13.5px;line-height:15.8px}
.poem{left:0;width:1200px;top:1991px;text-align:center;font-size:13.5px;line-height:15.8px}
.poem h3{font-size:14px;font-weight:600;margin-bottom:16px}
.funded{left:161px;top:2488px;font-size:14px;font-weight:600}
.badge{top:2517px;height:40px;border-radius:4px}
.footer{left:0;top:2576px;width:1200px;height:132px;background:var(--green-dark);color:var(--white)}
.footer-addr{left:66px;top:46px;font-size:13.5px;line-height:15.8px}
.footer-links a{position:absolute;right:67px;font-size:13.5px;color:var(--white);text-decoration:none}
</style>
</head>
<body>

<a class="abs btn-contact">Kontakt</a>

<div class="abs brand">
  <span class="brand-dot"></span>
  <span class="brand-name">(Un)gesehene Schwestern<br>Chemnitz und Umgebung</span>
</div>

<nav class="nav">
  <a style="left:350px;top:258px" aria-label="Startseite">
    <svg width="30" height="28" viewBox="0 0 30 28"><path d="M15 1 L29 13 V27 H1 V13 Z" fill="#4fb487"/><rect x="11" y="17" width="8" height="10" fill="#fff"/></svg>
  </a>
  <a style="left:477px;top:259px">Über uns</a>
  <a style="left:635px;top:259px">Das Team</a>
  <a style="left:808px;top:259px">Das Trauma</a>
  <a style="left:333px;top:317px">Hörschädigung</a>
  <a style="left:556px;top:317px">Netzwerkpartner</a>
  <a style="left:748px;top:317px">Aktuelles</a>
  <a style="left:900px;top:317px">Förderer</a>
</nav>

<div class="abs hero-bg"></div>
<h1 class="abs hero-title">(un)gesehene Schwestern</h1>
<h2 class="abs hero-sub">Die Selbsthilfegruppe in Chemnitz<br>und Umland</h2>
<p class="abs hero-text">Stellt man sich einen Wald vor, mit vielen Bäumen, darunter junge und alte, mit teils kraftvollen, mehr oder weniger kränkelnden Wurzeln, welche das Bedürfnis nach Wärme, Licht, Wasser und Dünger haben, einem nährenden Umfeld angehören und dem Sturm trotzen zu wollen, dann kann man sich die Motivation der Frauen, eine SHG gründen zu wollen vorstellen!</p>
<p class="abs hero-date">Sie haben es am 23. April 2022 getan!</p>
<div class="abs illus" role="img" aria-label="Illustration: zwei Frauen in Sprechblasen im Austausch" style="left:767px;top:483px;width:279px;height:305px;background:linear-gradient(160deg,#d8f0ef 0%,#f6d7d8 50%,#cfeeee 100%)"></div>

<h2 class="abs section-title">Wer wir sind</h2>

<div class="abs illus" role="img" aria-label="Illustration: Porträt der Leiterin" style="left:261px;top:1019px;width:77px;height:95px;background:linear-gradient(180deg,#fbe3a4,#fde0d0)"></div>
<div class="abs illus" role="img" aria-label="Illustration: Porträt der Stellvertreterin" style="left:454px;top:1021px;width:77px;height:93px;background:linear-gradient(180deg,#6a2a4a,#fbe0d4)"></div>
<div class="abs illus" role="img" aria-label="Illustration: fünf Frauen in Bewegung" style="left:662px;top:1025px;width:273px;height:117px;background:linear-gradient(90deg,#e9d4d6,#d3efe8,#e6d9e3)"></div>

<div class="abs card" style="left:245px;top:1141px;width:158px;height:49px">Leiterin:<br>Carola Weinhart</div>
<div class="abs card card-phone" style="left:245px;top:1197px;width:165px;height:38px">
  <svg width="18" height="18" viewBox="0 0 24 24"><path d="M6.6 10.8a15 15 0 006.6 6.6l2.2-2.2a1 1 0 011-.25 11.4 11.4 0 003.6.57 1 1 0 011 1V20a1 1 0 01-1 1A17 17 0 013 4a1 1 0 011-1h3.5a1 1 0 011 1c0 1.25.2 2.45.57 3.57a1 1 0 01-.25 1z" fill="#2f2f35"/></svg>
  <span>+ 49 151 00482715</span>
</div>
<div class="abs card" style="left:438px;top:1141px;width:153px;height:49px">Stellvertreterin:<br>Jana Brückner</div>
<div class="abs card card-phone" style="left:438px;top:1197px;width:165px;height:38px">
  <svg width="18" height="18" viewBox="0 0 24 24"><path d="M6.6 10.8a15 15 0 006.6 6.6l2.2-2.2a1 1 0 011-.25 11.4 11.4 0 003.6.57 1 1 0 011 1V20a1 1 0 01-1 1A17 17 0 013 4a1 1 0 011-1h3.5a1 1 0 011 1c0 1.25.2 2.45.57 3.57a1 1 0 01-.25 1z" fill="#2f2f35"/></svg>
  <span>+ 49 174 0036218</span>
</div>
<div class="abs card" style="left:653px;top:1156px;width:281px;height:79px">5 weitere Frauen mit speziellen Arbeitsaufgaben in Bereichen Organisation, Behördenkorresponden, Kooperation, u.a.</div>

<a class="abs mail">
  <svg width="22" height="17" viewBox="0 0 22 17"><rect x="1" y="1" width="20" height="15" rx="1.5" fill="none" stroke="#fff" stroke-width="1.6"/><path d="M1.5 2 L11 9 L20.5 2" fill="none" stroke="#fff" stroke-width="1.6"/></svg>
  <span>schwestern-chemnitz@beispielpost.de</span>
</a>

<section>
  <div class="abs band-green"></div>
  <div class="abs band-pink"></div>
  <h2 class="abs focus-title">Inhaltliche Schwerpunkte</h2>
  <div class="abs focus-text">
    <p>Zurück in das ICH finden mit Unterstützung<br>der Netzwerkpartner bzw. Traumaverbund Westland:</p>
    <ul>
      <li>Aufklärung</li><li>Erkennen</li><li>Benennen</li>
      <li>Handeln/ Vermittlung von Behandlung</li>
      <li>Vermittlung von Rehabilitation</li><li>Rückfallprävention</li>
    </ul>
  </div>
  <h2 class="abs goals-title">Kurzfristige und<br>langfristige Ziele</h2>
  <ul class="abs goals-list">
    <li>Förderung gesunder Beziehung über Respekt und Achtsamkeit</li>
    <li>Strategien einer gewaltfreien Kommunikation erlernen und anwenden</li>
    <li>Unterschiede tolerieren lernen</li>
    <li>Förderung der individuellen Entwicklung</li>
    <li>Auseinandersetzung mit eigenen Schattenseiten</li>
    <li>Förderung von Verantwortungsbewusstsein</li>
    <li>Akzeptanz der Realität und Öffnung für Lösungswege</li>
    <li>Lebensfreude und Leichtigkeit</li>
    <li>Gemeinschaft</li>
    <li>Geben und Nehmen</li>
    <li>Aufbau und Erhaltung von Selbstwert, Selbstsicherheit u. a. m.</li>
  </ul>
  <div class="abs illus" role="img" aria-label="Illustration: Gießkanne über einem Blumentopf mit Setzlingen" style="left:883px;top:1550px;width:257px;height:290px;background:linear-gradient(200deg,#f7a3a9 0%,#f6b8c7 55%,#f28c95 100%)"></div>
</section>

<div class="abs poem">
  <h3>Spiegelbild</h3>
  <p>"Siehst du, so läuft es<br>Siehst du, wie das Schweigen wirkt,<br>wie das Lachen Funken sprühen lässt<br>Ich zeige, was ich sehe<br>Ich sehe, was ich zeige<br>Du findest Dich in mir und die Antwort auf deine Fragen"</p>
</div>
<div class="abs illus" role="img" aria-label="Illustration: zwei rosa Monstera-Blätter mit gepunkteten Linien" style="left:473px;top:2134px;width:257px;height:273px;border-radius:40%;background:radial-gradient(circle at 45% 60%,#f48a98 0%,#f5b3bb 50%,#ffffff 100%)"></div>

<p class="abs funded">gefördert durch:</p>
<div class="abs badge" role="img" aria-label="Förderpartner 1" style="left:150px;width:160px;background:#2f9a5a"></div>
<div class="abs badge" role="img" aria-label="Förderpartner 2" style="left:331px;width:93px;background:#f2c94c"></div>
<div class="abs badge" role="img" aria-label="Förderpartner 3" style="left:447px;width:138px;background:#1e73be"></div>
<div class="abs badge" role="img" aria-label="Förderpartner 4" style="left:609px;width:167px;background:#d7262e"></div>
<div class="abs badge" role="img" aria-label="Förderpartner 5" style="left:799px;width:96px;background:#6ab04c"></div>
<div class="abs badge" role="img" aria-label="Förderpartner 6" style="left:921px;width:122px;background:#2d5fa8"></div>

<footer class="abs footer">
  <p class="abs footer-addr">Verbund Hörgeschädigter Muldental e.V.<br>Lindenallee 14<br>09120 Chemnitz</p>
  <div class="footer-links">
    <a style="top:28px">Impressum</a>
    <a style="top:60px">Datenschutz</a>
    <a style="top:93px">Kontakt</a>
  </div>
</footer>

</body>
</html>
```